Visitenkarten-Design für Eventcatering & Gemeinschaftsverpflegung
Wir sind sehr zufrieden mit Tolvi. Extrawünsche wurden zügig und sehr genau bearbeitet. Jederzeit gerne wieder:)
Zielgruppe
Wir sind ein kreatives und aufstrebendes Unternehmen.
Seit jahren sind wir im Eventcatering und der Gemeinschaftsverpflegung tätig.
Als Marktführer kochen wir super leckeres Mittagessen für Grundschulen und Kindertagesstätten in Berlin und Brandenburg und bewirtschaften mehrere Betriebsrestaurants.
Wir sind sehr krativ und bleiben nie stehen, so bereichern wir die Gastronomie in allen
Bereichen mit immer neuen innovativen Ideen und der Leidenschaft zum gesunden und leckeren Essen.
We are a creative and ambitious company.
We have been active in event catering and community catering for years.
As the market leader, we cook delicious lunches for elementary schools and day-care centers in Berlin and Brandenburg and we run several company restaurants.
We are very creative and never stand still, this is how we enrich the gastronomy in all of them
areas with new, innovative ideas and a passion for healthy and delicious food.
Aufgabenstellung
Wir möchten gern die Rottöne aus unserem Logo wiederfinden.
Unser Logo darf im Vordergrund stehen.
We would like to find the red tones from our logo again.
Our logo can be in the foreground.

```html
<!DOCTYPE html>
<html lang="de">
<head>
<meta charset="utf-8">
<title>Rotkost Catering – Visitenkarte</title>
<link rel="stylesheet" href="https://fonts.googleapis.com/css2?family=Poppins:wght@400;600;700&display=swap">
<style>
  :root {
    --red: #d42a2a;
    --red-dark: #a81c1f;
    --red-light: #e44a44;
    --white: #ffffff;
    --paper: #f3f3f3;
    --ink: #333333;
    --stage: #e9e6e3;
  }
  * { box-sizing: border-box; margin: 0; padding: 0; }
  html, body { width: 1200px; height: 800px; overflow: hidden; }
  body {
    background: var(--stage);
    font-family: "Poppins", sans-serif;
    position: relative;
  }
  .card {
    position: absolute;
    width: 510px;
    height: 330px;
    border-radius: 4px;
    overflow: hidden;
    box-shadow: 0 10px 30px rgba(0,0,0,.18);
  }
  .card-front { left: 50px; top: 200px; background: linear-gradient(135deg, var(--white), var(--paper)); }
  .card-back { left: 640px; top: 200px; }
  .card svg.shape { position: absolute; inset: 0; }
  .person { position: absolute; left: 40px; top: 110px; }
  .person-name { color: var(--red); font-weight: 700; font-size: 22px; }
  .person-role { color: var(--ink); font-size: 15px; }
  .contact { position: absolute; left: 285px; top: 38px; list-style: none; font-size: 13px; font-weight: 600; color: var(--ink); }
  .contact li { display: flex; align-items: center; gap: 8px; margin-bottom: 4px; }
  .contact svg { width: 12px; height: 12px; fill: var(--red); }
  .brand { display: flex; align-items: center; gap: 8px; font-weight: 700; white-space: nowrap; }
  .brand-mark { width: 22px; height: 22px; background: var(--red); border-radius: 3px; flex: none; }
  .card-front .brand { position: absolute; left: 240px; top: 108px; font-size: 21px; color: var(--ink); }
  .services {
    position: absolute; left: 215px; top: 244px; width: 300px;
    color: var(--white); font-weight: 600; font-size: 11.5px; text-align: center;
    line-height: 1.6; white-space: nowrap;
    transform: rotate(-17deg); transform-origin: center center;
  }
  .card-back .brand { position: absolute; left: 130px; top: 120px; font-size: 34px; color: var(--white); }
  .card-back .brand-mark { width: 30px; height: 30px; background: var(--white); }
  .web {
    position: absolute; left: 300px; top: 300px;
    color: var(--red); font-weight: 600; font-size: 15px;
    transform: rotate(-38deg); transform-origin: left top;
  }
  .logo-line {
    position: absolute; left: 50px; top: 620px;
    font-size: 48px; color: #1c1c1c;
  }
  .logo-line .brand-mark { width: 48px; height: 48px; border-radius: 6px; }
</style>
</head>
<body>

<section class="card card-front">
  <svg class="shape" width="510" height="330" viewBox="0 0 510 330">
    <defs>
      <linearGradient id="frontRed" x1="0" y1="1" x2="1" y2="0">
        <stop offset="0" stop-color="var(--red-dark)"/>
        <stop offset=".5" stop-color="var(--red)"/>
        <stop offset="1" stop-color="var(--red-light)"/>
      </linearGradient>
    </defs>
    <path role="img" aria-label="Rote Fläche mit dezent eingedruckten Speisen und Tellern"
          d="M150 330 L176 255 L192 276 Q340 235 510 165 L510 330 Z" fill="url(#frontRed)"/>
  </svg>
  <div class="person">
    <p class="person-name">Lena Beispiel</p>
    <p class="person-role">Director</p>
  </div>
  <ul class="contact">
    <li><svg viewBox="0 0 24 24"><path d="M6.6 10.8a15 15 0 0 0 6.6 6.6l2.2-2.2c.3-.3.7-.4 1-.2 1.1.4 2.3.6 3.6.6.6 0 1 .4 1 1V20c0 .6-.4 1-1 1A17 17 0 0 1 3 4c0-.6.4-1 1-1h3.5c.6 0 1 .4 1 1 0 1.3.2 2.5.6 3.6.1.3 0 .7-.2 1z"/></svg>030 / 512 778 40</li>
    <li><svg viewBox="0 0 24 24"><path d="M2 5h20v14H2z M2 5l10 8 10-8" stroke="#fff" stroke-width="1.5"/></svg>info@rotkost-catering.de</li>
  </ul>
  <div class="brand"><span class="brand-mark"></span>Rotkost Catering</div>
  <p class="services">Oberschulen - Grundschulen - Kindergarten<br>Betriebsgastronomie - Tagungsraum</p>
</section>

<section class="card card-back">
  <svg class="shape" width="510" height="330" viewBox="0 0 510 330">
    <defs>
      <radialGradient id="backRed" cx=".3" cy=".2" r=".9">
        <stop offset="0" stop-color="var(--red-light)"/>
        <stop offset="1" stop-color="var(--red-dark)"/>
      </radialGradient>
    </defs>
    <rect role="img" aria-label="Rote Fläche mit dezent eingedruckten Speisen und Tellern"
          width="510" height="330" fill="url(#backRed)"/>
    <path d="M180 330 L200 268 L214 288 Q390 250 510 120 L510 330 Z" fill="var(--white)"/>
  </svg>
  <div class="brand"><span class="brand-mark"></span>Rotkost Catering</div>
  <p class="web">rotkost-catering.de</p>
</section>

<div class="brand logo-line"><span class="brand-mark"></span>Rotkost Catering</div>

</body>
</html>
```